New homepage design - Cobalt Sages

- we would like to have a new website layout of the existing one: www.cobaltsages.ch
the new layout should have the following parameters:
- we want it to be minimalistic
- clear lines
- not too colourful (eventually also more in grey tone?)

our company: cobalt sages
- cobalt sages is an organizational consulting company and we work with organizations and individuals alike
- we are headquartered in the engadine
- examples: www.pelmartine.nyc, www.trodwickandhale.com, www.femorasix.com, www.daryluntley.website,

Target Market(s)

Companies

Industry/Entity Type

Consulting

Number of Pages Required

1 page

Font styles to use
Sans Serif

Colors

Designer to choose only greyscale colors for use in the design.

Requirements
Must have
• A minimalistic design
Nice to have
• minimalistic and slick
Should not have
• not too many colours

```html
<!DOCTYPE html>
<html lang="en">
<head>
<meta charset="utf-8">
<title>Cobalt Sages – Rise From Growth To Purpose</title>
<link href="https://fonts.googleapis.com/css2?family=Josefin+Sans:wght@300;400;600&family=Source+Sans+3:wght@400;600&display=swap" rel="stylesheet">
<style>
:root{
  --ink:#1d1d1d;
  --text:#2f2f2f;
  --muted:#6a6a6a;
  --btn:#8d8d8d;
  --bar:#3a3a3a;
  --bar-light:#7c7c7c;
  --line:#dcdcdc;
  --footer:#333333;
  --white:#ffffff;
  --head:"Josefin Sans",sans-serif;
  --body:"Source Sans 3",sans-serif;
}
*{box-sizing:border-box;margin:0;padding:0}
html,body{width:1200px;height:3728px;overflow:hidden}
body{background:var(--white);color:var(--text);font-family:var(--body);position:relative}
.abs{position:absolute}
.wrap{position:absolute;left:172px;width:856px}
h2.section-title{font-family:var(--head);font-weight:600;font-size:33px;letter-spacing:1px;color:var(--ink);text-align:center;position:absolute;left:0;width:1200px}
.lead{font-size:13px;line-height:22.5px;text-align:center;color:var(--text)}
.btn{display:inline-block;background:var(--btn);color:var(--white);font-family:var(--head);font-weight:600;font-size:13px;letter-spacing:.3px;padding:13px 10px 10px;border-radius:2px;text-decoration:none}

/* header */
.topbar{left:574px;top:0;height:51px;display:flex}
.topbar .date{background:var(--bar);color:#fff;font-weight:600;font-size:15px;padding:16px 16px 0 34px;clip-path:polygon(0 0,100% 0,100% 100%,22px 100%);width:238px;display:flex;gap:8px}
.topbar .mail{background:var(--bar-light);color:#fff;font-weight:600;font-size:15px;padding:16px 30px 0 14px;clip-path:polygon(0 0,100% 0,calc(100% - 18px) 100%,0 100%);margin-left:2px;width:214px;display:flex;gap:8px}
.brand{left:172px;top:90px}
.brand-name{display:flex;align-items:center;gap:10px;font-family:var(--head);font-weight:300;font-size:29px;letter-spacing:1px;color:#4a4a4a}
.brand-name .mark{width:14px;height:14px;border:1.5px solid #4a4a4a}
.brand-tag{font-family:var(--head);font-size:11px;letter-spacing:2.2px;color:#4a4a4a;margin-top:4px}
.nav{right:172px;top:98px;display:flex;gap:16px;font-size:15.5px;font-weight:600;color:var(--ink)}

/* hero */
.hero{left:0;top:148px;width:1200px;height:542px;background:linear-gradient(180deg,#ededed 0%,#e4e4e4 55%,#f2f2f2 78%,#dcdcdc 100%)}
.hero-title{position:absolute;top:106px;width:100%;text-align:center;font-family:var(--head);font-weight:400;font-size:44px;letter-spacing:7px;color:var(--ink)}
.hero-plants{position:absolute;left:290px;top:215px;width:620px;height:235px;background:linear-gradient(180deg,#7f8c70 0%,#a5ad98 45%,#d9d9d9 60%,#f1f1f1 100%);border-radius:6px;opacity:.75}
.hero-shelf{position:absolute;left:0;top:455px;width:100%;height:22px;background:linear-gradient(180deg,#f7f7f7,#cfcfcf)}

/* pillars */
.pillars{left:172px;top:1004px;width:856px;height:340px}
.hex{position:absolute;top:0;width:286px;height:340px}
.hex .shape{position:absolute;inset:0;clip-path:polygon(50% 0,100% 25%,100% 75%,50% 100%,0 75%,0 25%);background:#9a9a9a}
.hex .fill{position:absolute;inset:0 0 6px 0;clip-path:polygon(50% 0,100% 25%,100% 75%,50% 100%,0 75%,0 25%)}
.hex .label{position:absolute;width:100%;text-align:center;color:#fff;font-family:var(--head);font-weight:600;font-size:25px;line-height:26px;letter-spacing:1px}
.pillar-btn{position:absolute;top:1367px}

/* retreats */
.retreat-scene{left:0;top:1505px;width:1200px;height:555px;background:linear-gradient(180deg,#fff 0%,#fff 30%,#c9c4bf 45%,#8c7e72 55%,#5c6472 68%,#8c97a6 80%,#3a4250 100%)}

/* testimonial */
.quote-box{left:172px;top:2195px;width:856px;height:104px;background:#fff;border-radius:8px;box-shadow:0 2px 12px rgba(0,0,0,.12)}
.quote-logo{position:absolute;left:6px;top:8px;width:144px;height:90px;border:1px solid #666;border-radius:8px;display:flex;align-items:center;justify-content:center;font-family:var(--body);font-weight:600;font-size:30px;color:#3f3f3f}
.quote-text{position:absolute;left:248px;top:28px;width:590px;font-size:14px;line-height:22.5px}
.quote-tail{left:388px;top:2298px;width:0;height:0;border-right:36px solid transparent;border-top:30px solid #fff;filter:drop-shadow(0 3px 2px rgba(0,0,0,.08))}
.quote-author{left:300px;top:2347px;width:192px;text-align:center}
.quote-author b{display:block;font-weight:600;font-size:15px}
.quote-author span{font-size:13.5px;color:var(--muted)}

/* media */
.media-img{left:172px;top:2585px;width:420px;height:300px;background:linear-gradient(160deg,#1f2a5a 0%,#1a1f44 60%,#2a3670 100%)}
.media-title{font-family:var(--head);font-weight:400;font-size:19.5px;line-height:25px;letter-spacing:.3px;color:var(--ink);text-align:center}
.media-date{font-size:15px;text-align:center;color:var(--text)}
.clip{left:608px;top:2885px;width:420px;height:297px;border:1.5px solid #222;background:linear-gradient(180deg,#fafafa 0%,#eeeeee 100%)}

/* footer */
.footer{left:0;top:3280px;width:1200px;height:448px;background:var(--footer);color:#fff}
.footer h4{font-family:var(--head);font-weight:600;font-size:18px;letter-spacing:.5px;position:absolute;top:73px}
.f-item{position:absolute;display:flex;gap:12px;font-size:12.5px;line-height:22px}
.f-icon{width:32px;height:32px;border-radius:50%;background:#fff;flex:none;display:flex;align-items:center;justify-content:center;margin-top:2px}
.news{position:absolute;left:768px;display:flex;gap:10px;font-size:12.5px;line-height:22px;width:260px}
.news::before{content:"";flex:none;margin-top:6px;border-left:8px solid #fff;border-top:5px solid transparent;border-bottom:5px solid transparent;height:0}
.f-rule{position:absolute;left:172px;top:349px;width:856px;height:1px;background:#9a9a9a}
.copy{position:absolute;top:409px;width:100%;text-align:center;font-size:12px}
</style>
</head>
<body>

<header>
  <div class="abs topbar">
    <div class="date">
      <svg width="14" height="14" viewBox="0 0 24 24" fill="none" stroke="#fff" stroke-width="2"><path d="M5 3h4l2 5-3 2a12 12 0 006 6l2-3 5 2v4a2 2 0 01-2 2A18 18 0 013 5a2 2 0 012-2z"/></svg>
      16.03.2022 – 19.03.2022
    </div>
    <div class="mail">
      <svg width="15" height="15" viewBox="0 0 24 24" fill="none" stroke="#fff" stroke-width="2"><rect x="3" y="5" width="18" height="14" rx="1"/><path d="M3 6l9 7 9-7"/></svg>
      info@cobaltsages.ch
    </div>
  </div>
  <div class="abs brand">
    <div class="brand-name"><span class="mark"></span>COBALT SAGES</div>
    <div class="brand-tag">RISE FROM GROWTH TO PURPOSE</div>
  </div>
  <nav class="abs nav"><span>Home</span><span>Cobalt Sages</span><span>Executive Circle</span><span>For Corporations</span><span>For individuals</span></nav>
</header>

<section class="abs hero">
  <h1 class="hero-title">RISE FROM GROWTH TO PURPOSE</h1>
  <div class="hero-plants" role="img" aria-label="Four potted succulents and a cactus on a white shelf"></div>
  <div class="hero-shelf"></div>
</section>

<h2 class="section-title" style="top:768px">COBALT SAGES</h2>
<p class="wrap lead" style="top:826px">We convert the speak of purpose and consciousness into solutions. We are deeply convinced that a life and work ethics based on the attitude of serving all stakeholders and developing high levels of inclusiveness, gratitude and consciousness would lead to more happiness and superior results for all.<br>Our own purpose is to focus on these topics for the benefit of companies and leaders alike, thus creating an increased level of self-awareness, responsibility, fairness and alignment.<br>Seeing leaders and companies intensely passionate for what they engage in and achieving results beyond what has been thought possible fills us with joy and gives us great fulfilment.</p>

<div class="abs pillars">
  <div class="hex" style="left:0">
    <div class="shape"></div>
    <div class="fill" role="img" aria-label="Team members joining hands in agreement" style="background:linear-gradient(180deg,#d8d8d8 0%,#7d7d7d 55%,#1e1e1e 80%,#111 100%)"></div>
    <div class="label" style="top:268px">TEAM</div>
  </div>
  <div class="hex" style="left:285px">
    <div class="shape"></div>
    <div class="fill" role="img" aria-label="Silhouettes of climbers with a flag on a summit at sunset" style="background:linear-gradient(180deg,#f1ddb8 0%,#d9a86e 40%,#3c2d22 65%,#111 100%)"></div>
    <div class="label" style="top:255px">WHY WE<br>DO IT</div>
  </div>
  <div class="hex" style="left:570px">
    <div class="shape"></div>
    <div class="fill" role="img" aria-label="Hands clapping in a cloud of chalk dust" style="background:linear-gradient(180deg,#4a4a4a 0%,#9c9c9c 40%,#2a2a2a 70%,#111 100%)"></div>
    <div class="label" style="top:255px">HOW WE<br>DO IT</div>
  </div>
</div>
<a class="btn pillar-btn" style="left:266px">READ MORE</a>
<a class="btn pillar-btn" style="left:551px">READ MORE</a>
<a class="btn pillar-btn" style="left:836px">READ MORE</a>

<div class="abs retreat-scene" role="img" aria-label="Snowy mountain valley at sunrise"></div>
<h2 class="section-title" style="top:1530px">RETREATS</h2>
<p class="wrap lead" style="top:1587px">Several times per year, we organize retreats that focus on conscious leadership, defining one’s vision, purpose and legacy.<br>The “Cobalt Sages-Retreats” embrace a holistic approach. The number of participants is limited to a maximum of 12 leaders per retreat in order to guarantee intimacy and intensity. Target participants are C-Level executives, senior corporate managers, entrepreneurs, politicians, artists and sports people. In short: people who resume responsibility, are role-models for others, want to initiate and move things, create sustainable value and commit to following their highest consciousness at all times. Nevertheless, throughout the retreat we focus on the human being rather than the role and function.</p>

<h2 class="section-title" style="top:2127px">TESTIMONIALS</h2>
<div class="abs quote-box">
  <div class="quote-logo">verdalis</div>
  <p class="quote-text">The retreat was an open and warm exchange between special individuals who follow their own ways that don’t necessarily correspond to standard career paths.</p>
</div>
<div class="abs quote-tail"></div>
<div class="abs quote-author"><b>Marcel Ostrander</b><span>COO, Brightlane Systems</span></div>

<h2 class="section-title" style="top:2487px">MEDIA &amp; PRESS</h2>

<div class="abs media-img" role="img" aria-label="Panel slide showing the moderator and five panellists of a digital leaders conference"></div>
<div class="abs" style="left:172px;top:2900px;width:420px">
  <div class="media-title">ALPINE CIRCLE OF MBAS: DIGITAL LEADERS CONFERENCE 2021</div>
  <div class="media-date" style="margin-top:8px">25. May 2021</div>
  <p class="lead" style="margin-top:8px">Alpine Circle of MBAs: Digital Leaders Conference 2021.<br>Panel hosted by Helena Brunner: The success factors of leading in digital times.</p>
  <div style="text-align:center;margin-top:14px"><a class="btn">READ MORE</a></div>
</div>

<div class="abs" style="left:608px;top:2618px;width:420px">
  <div style="text-align:center"><a class="btn">READ MORE</a></div>
  <p class="lead" style="margin-top:18px">Herr Renner, Sie haben bei zwei grossen Finanzadressen in Zürich gearbeitet und dann «Cobalt Sages» ins Leben gerufen. Wie kamen Sie auf diese Idee?<br>Die Idee ist mit meiner Geschäftspartnerin Helena.</p>
  <div class="media-date" style="margin-top:10px">19. January 2021</div>
  <div class="media-title" style="margin-top:10px">MAN SOLLTE NICHT VERGESSEN, VON ZEIT ZU ZEIT SEINE RITTERRÜSTUNG IN DEN KLEIDERSCHRANK ZU STELLEN</div>
</div>
<div class="abs clip" role="img" aria-label="Printed interview clipping from Capitalnote with a portrait of Tobias Renner"></div>

<footer class="abs footer">
  <h4 style="left:172px">ADDRESS</h4>
  <h4 style="left:468px">RETREATS</h4>
  <h4 style="left:768px">RECENT NEWS</h4>

  <div class="f-item" style="left:172px;top:113px">
    <span class="f-icon"><svg width="16" height="16" viewBox="0 0 24 24" fill="none" stroke="#333" stroke-width="2"><path d="M12 22s7-7 7-12a7 7 0 00-14 0c0 5 7 12 7 12z"/><circle cx="12" cy="10" r="2.5"/></svg></span>
    <div>Cobalt Sages Ltd.<br>Lindenhofweg 12<br>8002 Zurich</div>
  </div>
  <div class="f-item" style="left:172px;top:195px">
    <span class="f-icon"><svg width="14" height="14" viewBox="0 0 24 24" fill="none" stroke="#333" stroke-width="2"><path d="M5 3h4l2 5-3 2a12 12 0 006 6l2-3 5 2v4a2 2 0 01-2 2A18 18 0 013 5a2 2 0 012-2z"/></svg></span>
    <div>Telephone:<br>+41 44 555 20 40</div>
  </div>
  <div class="f-item" style="left:172px;top:262px">
    <span class="f-icon"><svg width="15" height="15" viewBox="0 0 24 24" fill="none" stroke="#333" stroke-width="2"><rect x="3" y="5" width="18" height="14" rx="1"/><path d="M3 6l9 7 9-7"/></svg></span>
    <div>Email:<br>info@cobaltsages.ch</div>
  </div>

  <div class="f-item" style="left:468px;top:113px">
    <span class="f-icon"><svg width="14" height="14" viewBox="0 0 24 24" fill="none" stroke="#333" stroke-width="2"><path d="M5 3h4l2 5-3 2a12 12 0 006 6l2-3 5 2v4a2 2 0 01-2 2A18 18 0 013 5a2 2 0 012-2z"/></svg></span>
    <div>Cobalt Sages:<br>16.03.2022 – 19.03.2022<br>08.06.2022 – 11.06.2022<br>28.09.2022 – 01.10.2022</div>
  </div>
  <div class="f-item" style="left:468px;top:218px">
    <span class="f-icon"><svg width="14" height="14" viewBox="0 0 24 24" fill="none" stroke="#333" stroke-width="2"><path d="M5 3h4l2 5-3 2a12 12 0 006 6l2-3 5 2v4a2 2 0 01-2 2A18 18 0 013 5a2 2 0 012-2z"/></svg></span>
    <div>Clear Summit Retreats<br>02.03.2022 – 05.03.2022 (Level I)<br>14.09.2022 – 17.09.2022 (Level III)</div>
  </div>
  <div class="f-item" style="left:468px;top:300px">
    <span class="f-icon"><svg width="14" height="14" viewBox="0 0 24 24" fill="none" stroke="#333" stroke-width="2"><path d="M5 3h4l2 5-3 2a12 12 0 006 6l2-3 5 2v4a2 2 0 01-2 2A18 18 0 013 5a2 2 0 012-2z"/></svg></span>
    <div>Walk to Realign<br>16.06.2022 – 19.06.2022</div>
  </div>

  <div class="news" style="top:113px">Alpine Circle of MBAs: Digital Leaders Conference 2021</div>
  <div class="news" style="top:173px">Man sollte nicht vergessen, von Zeit zu Zeit seine Ritterrüstung in den Kleiderschrank zu stellen</div>

  <div class="f-rule"></div>
  <div class="copy">Copyrights @ Cobalt Sages. All Rights Reserved.</div>
</footer>

</body>
</html>
```